business card for law firm that reflects the web site -www.MarlaQuentby.com. That is pleasant to read

We need a business card for a small law firm. Your company designed our logo - tree of life - which I can provide to the designers. The card should be on both sides. Use the coloring from the web site (www.MarlaQuentby.com) and logo (I have several formats). I am attaching the logo, but not sure what format to use.

First side name of firm: Law Office of M.K. Quentby, P.A. 4819 West Pallisor, Suite 300, Phoenix, AZ 85016, Phone: 602.555.3841, Fax: 602.555.7290, web site: www.MarlaQuentby.com, email: MQuentby@MarlaQuentby.com.
Marla K. Quentby Bankruptcy and Foreclosure Attorney & Counselor.
Back side (perhaps vertical) the logo and then Notes with lines. At the bottom: Proud to help people and small businesses file for bankruptcy protection. We are a debt relief agency.
Updates

I have several versions of the logo. Will be happy to share whatever you need. Added Sunday, April 3, 2016

Target Market(s)

everyone

Industry/Entity Type

Legal

Contact Information for Business Card

I prefer something unique (rounded edges, design that adopts my web site - www.MarlaQuentby.com.

Font styles to use
Serif

Requirements
Must have
• First side name of firm: Law Office of M.K. Quentby, P.A. 4819 West Pallisor, Suite 300, Phoenix, AZ 85016, Phone: 602.555.3841, Fax: 602.555.7290, web site: www.MarlaQuentby.com, email: MQuentby@MarlaQuentby.com.
• Marla K. Quentby Bankruptcy and Foreclosure Attorney & Counselor.
• Back side (perhaps vertical) the logo and then Notes with lines. At the bottom: Proud to help people and small businesses file for bankruptcy protection. We are a debt relief agency.
• Green and brown colors that reflect the web site: www.MarlaQuentby.com
Should not have
• Type so small that older people cannot read.

```html
<!DOCTYPE html>
<html lang="en">
<head>
<meta charset="utf-8">
<title>Law Office of M.K. Quentby, P.A. – Business Card</title>
<link rel="stylesheet" href="https://fonts.googleapis.com/css2?family=Crimson+Text:wght@400;600;700&family=Libre+Franklin:wght@600;700&display=swap">
<style>
  :root {
    --page: #ffffff;
    --sage-top: #b4b6a2;
    --sage-mid: #e6e7dc;
    --card-white: #ffffff;
    --mauve: #a891a4;
    --forest: #1f3b18;
    --brown: #231510;
    --brown-ring: #3a2119;
    --rule-rose: #6b4a4a;
    --rule-dark: #2b2320;
    --ink: #111111;
    --cream: #ffffff;
  }
  * { margin: 0; padding: 0; box-sizing: border-box; }
  html, body {
    width: 1200px; height: 710px; overflow: hidden; background: var(--page);
  }
  .sheet { position: relative; width: 1200px; height: 710px; }

  /* Front */
  .card-front {
    position: absolute; left: 379px; top: 98px; width: 252px; height: 145px;
    border-radius: 8px; overflow: hidden;
    font-family: "Crimson Text", Georgia, serif;
  }
  .front-head {
    position: absolute; inset: 0 0 73px 0;
    background: linear-gradient(to bottom, var(--sage-top), var(--card-white));
  }
  .front-foot {
    position: absolute; left: 0; right: 0; bottom: 0; height: 73px;
    background: var(--brown); color: var(--cream);
  }
  .brand-mark {
    position: absolute; left: 9px; top: 4px; width: 64px; height: 64px;
    border: 3px solid var(--brown-ring); border-radius: 50%;
    display: flex; align-items: center; justify-content: center; text-align: center;
    color: var(--brown-ring); font-weight: 700; font-size: 11px; line-height: 1.05;
  }
  .firm-title {
    position: absolute; left: 106px; top: 2px; color: var(--forest);
    font-weight: 700; font-size: 19px; line-height: 1;
  }
  .firm-name {
    position: absolute; left: 106px; top: 24px; color: var(--forest);
    font-size: 16px; line-height: 1;
  }
  .firm-name small { font-size: 10px; }
  .attorney {
    position: absolute; right: 5px; top: 46px; text-align: right; color: var(--forest);
  }
  .attorney-name { font-size: 12px; line-height: 1; }
  .attorney-role { font-size: 6.5px; font-weight: 700; color: var(--ink); line-height: 1.2; }

  .web { position: absolute; left: 14px; top: 13px; font-size: 10px; font-weight: 700; line-height: 1.25; }
  .contact-block { position: absolute; right: 10px; top: 5px; text-align: center; }
  .contact-label { font-size: 7.5px; font-weight: 700; line-height: 1; }
  .contact-number { font-size: 12px; font-weight: 700; line-height: 1.1; margin-bottom: 1px; }
  .address { position: absolute; left: 21px; bottom: 8px; font-size: 8.5px; }

  /* Back */
  .card-back {
    position: absolute; left: 706px; top: 0; width: 144px; height: 252px;
    border-radius: 8px; overflow: hidden;
    background: linear-gradient(to bottom, var(--sage-top) 0%, var(--sage-mid) 30%, var(--card-white) 48%, var(--card-white) 55%, var(--mauve) 100%);
    font-family: "Crimson Text", Georgia, serif;
  }
  .back-mark {
    position: absolute; left: 28px; top: 6px; width: 88px; height: 88px;
    border: 4px solid var(--brown-ring); border-radius: 50%;
    display: flex; align-items: center; justify-content: center; text-align: center;
    color: var(--brown-ring); font-weight: 700; font-size: 15px; line-height: 1.05;
  }
  .notes-title {
    position: absolute; left: 0; right: 0; top: 96px; text-align: center;
    font-size: 9px; font-weight: 600; color: var(--ink);
  }
  .notes-title span { border-bottom: 1px solid var(--ink); }
  .notes-lines { position: absolute; left: 13px; top: 117px; }
  .tagline {
    position: absolute; left: 0; right: 0; top: 226px; text-align: center;
    font-family: "Libre Franklin", Arial, sans-serif; font-weight: 700;
    font-size: 5.2px; line-height: 1.3; color: var(--ink);
  }
</style>
</head>
<body>
<main class="sheet">

  <section class="card-front" aria-label="Business card front">
    <div class="front-head">
      <div class="brand-mark">M.K.<br>Quentby</div>
      <h1 class="firm-title">Law Office of</h1>
      <p class="firm-name">M.K. Quentby, <small>P.A.</small></p>
      <div class="attorney">
        <p class="attorney-name">Marla K. Quentby</p>
        <p class="attorney-role">Bankruptcy and Foreclosure Attorney &amp; Counselor</p>
      </div>
    </div>
    <div class="front-foot">
      <p class="web">www.MarlaQuentby.com<br>MQuentby@MarlaQuentby.com</p>
      <div class="contact-block">
        <p class="contact-label">Phone</p>
        <p class="contact-number">602.555.3841</p>
        <p class="contact-label">Fax</p>
        <p class="contact-number">602.555.7290</p>
      </div>
      <p class="address">4819 West Pallisor, Suite 300, Phoenix, AZ 85016</p>
    </div>
  </section>

  <section class="card-back" aria-label="Business card back">
    <div class="back-mark">M.K.<br>Quentby</div>
    <h2 class="notes-title"><span>NOTES</span></h2>
    <svg class="notes-lines" width="118" height="108" viewBox="0 0 118 108">
      <g stroke-width="0.8">
        <line x1="0" y1="1" x2="118" y2="1" stroke="var(--rule-rose)"/>
        <line x1="0" y1="14" x2="118" y2="14" stroke="var(--rule-dark)"/>
        <line x1="0" y1="27" x2="118" y2="27" stroke="var(--rule-rose)"/>
        <line x1="0" y1="40" x2="118" y2="40" stroke="var(--rule-dark)"/>
        <line x1="0" y1="53" x2="118" y2="53" stroke="var(--rule-dark)"/>
        <line x1="0" y1="66" x2="118" y2="66" stroke="var(--rule-dark)"/>
        <line x1="0" y1="79" x2="118" y2="79" stroke="var(--rule-dark)"/>
        <line x1="0" y1="92" x2="118" y2="92" stroke="var(--rule-dark)"/>
        <line x1="0" y1="105" x2="118" y2="105" stroke="var(--rule-dark)"/>
      </g>
    </svg>
    <p class="tagline">Proud to help people and small businesses<br>file for bankruptcy protection.<br>We are a debt relief agency.</p>
  </section>

</main>
</body>
</html>
```